Lantern Reach Website

Looking for a website design that clearly and powerfully portrays our unique and effective indoor advertising billboards in our network.

Our Classic Billboards and Wall Boards are strategically placed in high traffic areas of restaurants, pubs, nightclubs, fitness clubs, colleges & universities, and sports facilities.

Lantern Reach Network is our new name. Our current site is www.brightpostmarketing.ca
with our focus being entirely on our Out-of-Home Media Networks.

New website address will be www.lanternreach.ca

We need the following sections:
HOME

PRODUCTS (Drop down menu)
-Classic Billboards
-Wall Boards

NETWORKS (Drop down menu)
-Resto-Bar
-Sports
-Campus
-Casino

FEATURES

CAMPAIGNS

BECOME A PARTNER

CONTACT

Please include social media functions on the homepage such as twitter/facebook/linkdin

We will be supplying content and photos as required.

Our plan is to have you submit the homepage design to start with, and then we can start judging which styles we like the best and can start narrowing our list.

As a second round, we would like to ask the "finalists" to submit a second page (another section of the website) and to see how consistent you are in terms of the look and feel you proposed for the homepage.

Attached is our new logo.

Target Market(s)

Small Business Owners, Advertising Agencies, Media Buyers, Marketing Managers

Industry/Entity Type

Media

Number of Pages Required

1 page

Font styles to use
Sans Serif

Requirements
Must have
• Our Unique Network offers advertising solutions that feature:
• Guaranteed Readership,100% Gender Specific, Frequency, and Captive Audience. Purchasing advertising space in our network are small to medium business owners and advertising agencies booking on behalf of their clients.
• Site must be professional and modern looking.

```html
<!DOCTYPE html>
<html lang="en">
<head>
<meta charset="utf-8">
<title>Lantern Reach Network</title>
<link href="https://fonts.googleapis.com/css2?family=Quicksand:wght@500;600;700&family=Raleway:wght@400;500;600;700&display=swap" rel="stylesheet">
<style>
:root{
  --red:#c4161c;
  --dark:#2b2b2b;
  --text:#555;
  --muted:#9a9a9a;
  --line:#d6d6d6;
  --footer:#1f1f1f;
  --footer-deep:#141414;
  --white:#fff;
}
*{box-sizing:border-box;margin:0;padding:0}
html,body{width:1200px;height:2242px;overflow:hidden}
body{position:relative;background:var(--white);font-family:"Raleway",Arial,sans-serif;color:var(--text)}
.abs{position:absolute}
.heading{font-family:"Quicksand",Arial,sans-serif;font-weight:700;color:var(--dark);font-size:28px;letter-spacing:-.2px}
.heading em{font-style:normal;color:var(--red)}

/* header */
.site-header{position:absolute;left:0;top:0;width:1200px;height:98px;border-bottom:3px solid var(--red);background:var(--white)}
.brand{position:absolute;left:161px;top:33px;display:flex;align-items:center;gap:8px;font-family:"Quicksand",sans-serif;font-weight:700;font-size:23px;color:#555;line-height:1;white-space:nowrap}
.brand-dot{width:22px;height:22px;border-radius:50%;background:var(--red)}
.callbar{position:absolute;left:666px;top:14px;display:flex;align-items:center;height:32px}
.call-icon{width:30px;height:30px;border-radius:50%;border:1.5px solid var(--red);display:flex;align-items:center;justify-content:center}
.call-label{margin-left:10px;font-size:10.5px;color:#555;letter-spacing:.3px}
.call-number{margin-left:9px;font-size:20px;color:var(--dark);font-weight:500;letter-spacing:.3px}
.call-sep{width:1px;height:26px;background:var(--line);margin:0 15px 0 18px}
.social{display:flex;gap:6px}
.social span{display:block;width:28px;height:28px;border-radius:50%;background:var(--red)}
.main-nav{position:absolute;top:63px;left:0;font-family:"Quicksand",sans-serif;font-weight:600;font-size:14px;color:#333}
.main-nav a{position:absolute;white-space:nowrap;color:inherit;text-decoration:none}
.main-nav a.active{color:var(--red)}
.main-nav .caret{font-size:9px;margin-left:3px}

/* hero */
.hero{position:absolute;left:0;top:98px;width:1200px;height:450px;background:
  linear-gradient(180deg,#1c4f9c 0%,#2a66b6 22%,#c89a5c 40%,#e0b47a 62%,#c98e4e 78%,#1f5aa8 92%,#173f80 100%)}
.hero-caption{position:absolute;left:161px;top:395px;width:877px;height:54px;background:rgba(20,24,34,.82);display:flex;align-items:center;padding-left:19px;font-family:"Quicksand",sans-serif;font-weight:600;font-size:17px;color:#f0f0f0}
.hero-dots{position:absolute;right:22px;top:24px;display:flex;gap:7px}
.hero-dots i{width:7px;height:7px;background:#fff}
.hero-dots i.on{background:var(--red)}

/* dividers */
.divider{position:absolute;height:12px}
.divider::before{content:"";position:absolute;left:0;right:0;top:5px;height:2px;background:var(--line)}
.divider b{position:absolute;top:0;width:12px;height:12px;border-radius:50%;border:2px solid #bbb;background:var(--white)}

/* about */
.about-copy{position:absolute;left:150px;top:674px;width:900px;text-align:center;font-size:12px;line-height:19px}
.about-copy p{margin-bottom:11px}
.about-copy strong{color:var(--dark);font-weight:700}

/* products */
.products{position:absolute;left:0;top:871px;width:1200px;height:423px;background:linear-gradient(180deg,#e9e9e9,#f2f2f2 60%,#ececec)}
.tabs{position:absolute;left:451px;top:130px;display:flex;font-size:13px;font-weight:700;color:#222;letter-spacing:.2px}
.tab{height:40px;display:flex;align-items:center;justify-content:center;border-bottom:1px solid #aaa}
.tab.active{width:124px;border:1px solid #888;border-bottom:none;background:#f6f6f6}
.tab.plain{width:172px}
.tab-note{position:absolute;left:0;width:1200px;top:193px;text-align:center;font-size:11.5px}
.sub-heading{position:absolute;font-family:"Raleway",sans-serif;font-weight:600;font-size:21px;color:var(--dark)}
.ticks{position:absolute;list-style:none;font-size:12px;color:#444}
.ticks li{position:absolute;left:0;display:flex;gap:9px;white-space:nowrap}
.ticks svg{flex:none}
.board-photo{position:absolute;left:445px;top:238px;width:309px;height:133px;border:3px solid #d88;background:linear-gradient(180deg,#eef0ee 0%,#d9dcd8 45%,#b9bdb8 70%,#7d8a86 100%)}
.network-copy{position:absolute;left:791px;width:245px;font-size:12px;line-height:19.5px;color:#444}
.network-copy strong{color:#222}

/* effectiveness */
.eff-lead{position:absolute;left:161px;top:1421px;font-size:11.5px;font-weight:700;color:#222}
.eff-list{position:absolute;left:161px;top:0;list-style:none;font-size:12px;line-height:16.5px;color:#444}
.eff-list li{position:absolute;left:0;width:590px;padding-left:21px}
.eff-list svg{position:absolute;left:0;top:2px}
.col-rule{position:absolute;left:786px;top:1346px;width:1px;height:420px;background:#e2e2e2}
.poster{position:absolute;left:819px;top:1424px;width:219px;height:285px;border:1px solid #333;background:linear-gradient(180deg,#6d2c80,#5a1f6c 60%,#4b1a5a)}
.poster-name{position:absolute;left:819px;top:1724px;width:219px;text-align:center;font-size:15px;font-weight:700;color:#222}
.poster-dots{position:absolute;left:903px;top:1754px;display:flex;gap:6px}
.poster-dots i{width:8px;height:8px;border-radius:50%;border:1px solid #555}
.poster-dots i.on{background:var(--red);border-color:var(--red)}

/* footer */
.swoosh{position:absolute;left:0;top:1740px}
.footer{position:absolute;left:0;top:1930px;width:1200px;height:269px;background:var(--footer)}
.footer-base{position:absolute;left:0;top:2199px;width:1200px;height:43px;background:var(--footer-deep)}
.foot-title{position:absolute;top:1956px;font-family:"Quicksand",sans-serif;font-weight:600;font-size:14px;color:#eee;padding-bottom:8px;border-bottom:1px solid #444}
.quick-links{position:absolute;left:161px;top:1993px;list-style:none;font-size:11.5px;color:#ccc}
.quick-links li{height:33px;display:flex;gap:8px;align-items:flex-start}
.quick-links li::before{content:"";width:4px;height:4px;background:#888;margin-top:6px}
.field{position:absolute;left:327px;width:206px;background:#fff;font-size:9.5px;color:#999;padding:8px 9px}
.submit{position:absolute;left:327px;top:2139px;width:85px;height:29px;background:var(--red);color:#fff;font-size:11.5px;font-weight:700;display:flex;align-items:center;justify-content:center}
.contact-list{position:absolute;left:590px;top:1995px;list-style:none;font-size:11.5px;color:#ddd;line-height:19px}
.contact-list li{position:absolute;left:0;display:flex;gap:10px;white-space:nowrap}
.contact-list svg{flex:none;margin-top:3px}
.foot-brand{position:absolute;left:814px;top:2024px;display:flex;align-items:center;gap:7px;font-family:"Quicksand",sans-serif;font-weight:700;font-size:20px;color:#ddd;white-space:nowrap}
.foot-brand span.dot{width:18px;height:18px;border-radius:50%;background:#ddd}
.foot-social{position:absolute;left:876px;top:2097px;display:flex;gap:8px}
.foot-social span{width:27px;height:27px;border-radius:50%;background:var(--red)}
</style>
</head>
<body>
<svg width="0" height="0" style="position:absolute">
  <defs>
    <symbol id="tick" viewBox="0 0 14 14">
      <rect x="1" y="2" width="11" height="11" fill="none" stroke="#333" stroke-width="1.4"/>
      <path d="M3.5 7.5 L6.2 10.2 L13 2.5" fill="none" stroke="#222" stroke-width="2"/>
    </symbol>
  </defs>
</svg>

<header class="site-header">
  <div class="brand"><span class="brand-dot"></span>Lantern Reach Network</div>
  <div class="callbar">
    <span class="call-icon"><svg width="14" height="14" viewBox="0 0 24 24"><path d="M6.6 10.8a15 15 0 0 0 6.6 6.6l2.2-2.2a1 1 0 0 1 1-.25 11.4 11.4 0 0 0 3.6.57 1 1 0 0 1 1 1V20a1 1 0 0 1-1 1A17 17 0 0 1 3 4a1 1 0 0 1 1-1h3.5a1 1 0 0 1 1 1c0 1.25.2 2.45.57 3.57a1 1 0 0 1-.25 1z" fill="#c4161c"/></svg></span>
    <span class="call-label">CALL US NOW :</span>
    <span class="call-number">555.010.4420</span>
    <span class="call-sep"></span>
    <div class="social" aria-label="Social links"><span aria-label="Social link 1"></span><span aria-label="Social link 2"></span><span aria-label="Social link 3"></span></div>
  </div>
  <nav class="main-nav">
    <a class="active" style="left:444px">Home</a>
    <a style="left:518px">Products<span class="caret">&#9660;</span></a>
    <a style="left:621px">Networks<span class="caret">&#9660;</span></a>
    <a style="left:731px">Campaigns</a>
    <a style="left:840px">Become A Partner</a>
    <a style="left:990px">Contact</a>
  </nav>
</header>

<section class="hero" role="img" aria-label="Photo of an indoor basketball arena with blue seating and a wooden court">
  <div class="hero-caption">Over 1,000 Billboards 3 Targeted Networks Regional Coverage
    <div class="hero-dots"><i class="on"></i><i></i><i></i></div>
  </div>
</section>

<h2 class="heading abs" style="left:0;width:1200px;text-align:center;top:592px">About <em>Us</em></h2>
<div class="divider" style="left:161px;width:877px;top:639px"><b style="left:593px"></b></div>
<div class="about-copy">
  <p>Established in 1996, <strong>Brightpost Advertising Network</strong> is a Canadian out-of-home media company based in Kamloops, British Columbia.</p>
  <p><strong>Brightpost Advertising Network</strong> offers innovative and effective indoor Classic Billboards and Wallboards that are strategically placed in high traffic areas of restaurants, pubs, nightclubs, fitness clubs, colleges and universities, and sports arenas.</p>
  <p><strong>Brightpost Advertising Network</strong> offers high impact branding placements at high traffic properties throughout British Columbia.</p>
  <p><strong>Brightpost Advertising Network</strong> also specializes in the area of developing long-term revenue streams through the selling of sponsorship, supplier partnerships and naming rights packages</p>
</div>

<section class="products">
  <h2 class="heading abs" style="left:0;width:1200px;text-align:center;top:45px">Our <em>Products</em></h2>
  <div class="divider" style="left:161px;width:877px;top:92px"><b style="left:593px"></b></div>
  <div class="tabs"><div class="tab active">WALLBOARD</div><div class="tab plain">CLASSIC BILLBOARD</div></div>
  <p class="tab-note">48" x 96" billboards are strategically placed on facility walls.</p>
  <h3 class="sub-heading" style="left:161px;top:234px">Features</h3>
  <ul class="ticks" style="left:161px;top:273px">
    <li style="top:0"><svg width="14" height="14"><use href="#tick"/></svg>Visible to all users of the facility</li>
    <li style="top:42px"><svg width="14" height="14"><use href="#tick"/></svg>High Impact &amp; Full Colour</li>
    <li style="top:82px"><svg width="14" height="14"><use href="#tick"/></svg>Increases Brand Awareness</li>
  </ul>
  <div class="board-photo" role="img" aria-label="Photo of a wallboard ad mounted on an arena wall"></div>
  <h3 class="sub-heading" style="left:790px;top:234px">Networks</h3>
  <p class="network-copy" style="top:271px">Available in the <strong>Sports</strong> network</p>
  <p class="network-copy" style="top:296px">Lorem ipsum dolor sit amet, consectetuer adipiscing elit, sed diam nonummy nibh euismod tincidunt ut laoreet dolore.</p>
</section>

<h2 class="heading abs" style="left:161px;top:1340px">Effective<em>ness</em></h2>
<div class="divider" style="left:161px;width:596px;top:1386px"><b style="left:0"></b></div>
<p class="eff-lead">Effectiveness of Indoor Advertising...</p>
<ul class="eff-list">
  <li style="top:1466px"><svg width="14" height="14"><use href="#tick"/></svg>Indoor Advertising provides advertising messages during "social interaction" settings at bars, restaurants, nightclubs, health clubs, sports arenas and other venues.</li>
  <li style="top:1529px"><svg width="14" height="14"><use href="#tick"/></svg>Washroom advertising, captures the attention of the young and affluent 18 - 34 year old demographic. Often referred to as non-traditional advertising, washroom advertising is widely recognized as an extremely targeted, well-received advertising medium.</li>
  <li style="top:1608px"><svg width="14" height="14"><use href="#tick"/></svg>Viewers have made the decision to drop-in to a venue that suits their lifestyle, gender, or sports team preference, adding to the impact of the targeted message.</li>
  <li style="top:1671px"><svg width="14" height="14"><use href="#tick"/></svg>In addition, indoor advertising reaches consumers from an uncluttered, captive, eye-level vantage point, making it unavoidable - and magnifying the impact of the message.</li>
  <li style="top:1734px"><svg width="14" height="14"><use href="#tick"/></svg>Out-of-Home media is the most effective way to reach, engage and influence today's mobile and active consumer.</li>
</ul>
<div class="col-rule"></div>

<h2 class="heading abs" style="left:819px;top:1340px">Campa<em>igns</em></h2>
<div class="divider" style="left:819px;width:219px;top:1386px"><b style="left:0"></b></div>
<div class="poster" role="img" aria-label="Campaign poster for a smoothie brand on a purple background"></div>
<p class="poster-name">Grove Blend</p>
<div class="poster-dots"><i class="on"></i><i></i><i></i><i></i></div>

<svg class="swoosh" width="1200" height="200" viewBox="0 0 1200 200" aria-hidden="true">
  <path d="M0 22 C 180 110, 420 165, 720 172 C 430 178, 190 140, 0 82 Z" fill="#c4161c"/>
  <path d="M0 92 C 250 165, 520 192, 760 190 C 950 188, 1080 150, 1200 80 L1200 200 L0 200 Z" fill="#1f1f1f"/>
  <path d="M0 86 C 220 152, 480 182, 730 181" fill="none" stroke="#fff" stroke-width="4"/>
</svg>

<footer class="footer"></footer>
<div class="footer-base"></div>

<h4 class="foot-title" style="left:161px">Quick Links</h4>
<ul class="quick-links">
  <li>Home</li><li>Products</li><li>Networks</li><li>Campaigns</li><li>Become A Partner</li><li>Contact</li>
</ul>

<h4 class="foot-title" style="left:329px">Quick Contact</h4>
<div class="field" style="top:1997px;height:27px">Name*</div>
<div class="field" style="top:2033px;height:27px">Email*</div>
<div class="field" style="top:2069px;height:56px">Massage</div>
<div class="submit">Submit</div>

<h4 class="foot-title" style="left:590px">Contact Information</h4>
<ul class="contact-list">
  <li style="top:0"><svg width="10" height="13" viewBox="0 0 10 13"><path d="M5 0a5 5 0 0 1 5 5c0 3.5-5 8-5 8S0 8.5 0 5a5 5 0 0 1 5-5zm0 3a2 2 0 1 0 0 4 2 2 0 0 0 0-4z" fill="#ddd"/></svg><span>Suite #214, 480-1650<br>Ridgeway Drive<br>Kamloops, BC, V2C 4T8</span></li>
  <li style="top:70px"><svg width="11" height="11" viewBox="0 0 24 24"><path d="M6.6 10.8a15 15 0 0 0 6.6 6.6l2.2-2.2a1 1 0 0 1 1-.25 11.4 11.4 0 0 0 3.6.57 1 1 0 0 1 1 1V20a1 1 0 0 1-1 1A17 17 0 0 1 3 4a1 1 0 0 1 1-1h3.5a1 1 0 0 1 1 1c0 1.250.2 2.45.57 3.57a1 1 0 0 1-.25 1z" fill="#ddd"/></svg>555.010.4420 (Tel)</li>
  <li style="top:100px"><svg width="11" height="11" viewBox="0 0 24 24"><path d="M6.6 10.8a15 15 0 0 0 6.6 6.6l2.2-2.2a1 1 0 0 1 1-.25 11.4 11.4 0 0 0 3.6.57 1 1 0 0 1 1 1V20a1 1 0 0 1-1 1A17 17 0 0 1 3 4a1 1 0 0 1 1-1h3.5a1 1 0 0 1 1 1c0 1.25.2 2.45.57 3.57a1 1 0 0 1-.25 1z" fill="#ddd"/></svg>555.010.4421 (Fax)</li>
  <li style="top:130px"><svg width="11" height="11" viewBox="0 0 24 24"><path d="M6.6 10.8a15 15 0 0 0 6.6 6.6l2.2-2.2a1 1 0 0 1 1-.25 11.4 11.4 0 0 0 3.6.57 1 1 0 0 1 1 1V20a1 1 0 0 1-1 1A17 17 0 0 1 3 4a1 1 0 0 1 1-1h3.5a1 1 0 0 1 1 1c0 1.25.2 2.45.57 3.57a1 1 0 0 1-.25 1z" fill="#ddd"/></svg>800.555.0142 (Toll Free)</li>
  <li style="top:158px"><svg width="12" height="10" viewBox="0 0 12 10"><rect x=".5" y=".5" width="11" height="9" fill="none" stroke="#ddd"/><path d="M.5 .5 6 5.5 11.5 .5" fill="none" stroke="#ddd"/></svg>info@lanternreach.ca</li>
</ul>

<div class="foot-brand"><span class="dot"></span>Lantern Reach Network</div>
<div class="foot-social" aria-label="Social links"><span aria-label="Social link 1"></span><span aria-label="Social link 2"></span><span aria-label="Social link 3"></span></div>
</body>
</html>
```